WUVO Promotional flyer for students

We're looking for an 8.5" x 11" flyer that will be distributed to schools. Please see language to include in attached files.

Target Market(s)

The parents and teachers of high school students

Industry/Entity Type

Mental health

Font styles to use
Other font styles liked:
• Monserrat and Roboto Slab

Requirements
Must have
• See attached pdf for language to be included on the flyer. Please use the color palette from our website: www.watchwuvo.tv. Please include some imagery of students. Please ensure the
Nice to have
• Feel free to use any of the graphics provided. See our website for our brand look & feel: www.watchwuvo.tv

```html
<!DOCTYPE html>
<html lang="en">
<head>
<meta charset="utf-8">
<title>Fundraise with WUVO – Flyer</title>
<link rel="stylesheet" href="https://fonts.googleapis.com/css2?family=Roboto:wght@400;500;700;900&display=swap">
<style>
  :root {
    --page-bg: #e9ece8;
    --brand-blue: #35689a;
    --brand-blue-light: #4a86bb;
    --brand-orange: #e8742f;
    --brand-orange-light: #f09a49;
    --mist: rgba(200, 222, 240, 0.7);
    --ink-light: #ffffff;
    --ink-soft: #e6eef6;
  }
  * { box-sizing: border-box; margin: 0; padding: 0; }
  html, body { width: 1200px; height: 1200px; overflow: hidden; background: var(--page-bg); }
  body { font-family: "Roboto", Arial, sans-serif; }

  .flyer {
    position: absolute; left: 175px; top: 50px;
    width: 850px; height: 1100px; overflow: hidden;
    background: linear-gradient(160deg, var(--brand-blue-light) 0%, var(--brand-blue) 55%, #30608f 100%);
    box-shadow: 0 10px 30px rgba(0,0,0,0.18);
  }
  .hero-circle {
    position: absolute; left: -275px; top: -325px;
    width: 810px; height: 810px; border-radius: 50%;
    background: linear-gradient(200deg, var(--brand-orange-light) 0%, var(--brand-orange) 45%, #e56b2c 100%);
  }
  .headline {
    position: absolute; left: 70px; top: 88px;
    color: var(--ink-light); font-weight: 900; font-size: 56px;
    line-height: 0.92; letter-spacing: 0.5px; text-transform: uppercase;
  }
  .brand-mark {
    position: absolute; left: 712px; top: 22px;
    width: 108px; height: 108px; border-radius: 50%;
    background: var(--brand-orange);
    display: flex; align-items: center; justify-content: center;
    color: var(--ink-light); font-weight: 700; font-size: 34px; letter-spacing: -0.5px;
  }
  .photo {
    position: absolute; left: 345px; top: 155px;
    width: 480px; height: 480px; border-radius: 50%;
    background: linear-gradient(170deg, #eef0f2 0%, #c9cfd6 30%, #8c97a8 58%, #3a4558 82%, #1c2433 100%);
  }
  .accent-circle {
    position: absolute; left: 690px; top: 205px;
    width: 320px; height: 320px; border-radius: 50%;
    background: var(--mist);
  }
  .pledge {
    position: absolute; left: 170px; top: 712px;
    color: var(--ink-soft); font-weight: 900; font-size: 40px; line-height: 1.1;
  }
  .rule {
    position: absolute; left: 170px; top: 820px;
    width: 620px; height: 2px; background: var(--ink-soft);
  }
  .intro {
    position: absolute; left: 170px; top: 842px; width: 430px;
    color: var(--ink-soft); font-weight: 500; font-size: 19px; line-height: 1.62;
  }
  .corner-circle {
    position: absolute; left: 668px; top: 950px;
    width: 380px; height: 380px; border-radius: 50%;
    background: var(--brand-orange);
  }
  .web-address {
    position: absolute; left: 700px; top: 1050px;
    color: var(--ink-light); font-size: 15px; font-weight: 500;
  }
</style>
</head>
<body>
  <main class="flyer">
    <div class="hero-circle"></div>
    <h1 class="headline">Fundraise<br>with WUVO</h1>
    <div class="brand-mark">wuvo</div>
    <div class="photo" role="img" aria-label="Photo of a high school student talking with a counsellor who takes notes"></div>
    <div class="accent-circle"></div>
    <h2 class="pledge">50% of all proceeds<br>Go back to your school.</h2>
    <div class="rule"></div>
    <p class="intro">WUVO is a simple and effective way to<br>improve mental health. Your students<br>will learn valuable coping skills and<br>techniques from expert clinicians who<br>analyze real cases and share their<br>insights and advice.</p>
    <div class="corner-circle"></div>
    <p class="web-address">www.watchwuvo.tv</p>
  </main>
</body>
</html>
```